Business Card Design using new logo

As much as we'd like to think that treating everyone equally is the best strategy for fairness, the reality is that the differences in the lives of women and men have to be taken into account to ensure that organizations, programs, services, and yes, even public policy treat women and men in ways that achieve gender equity.

That's where ParityLumen - fairness metrics insight comes in. Using the data-driven tools of gender analysis, our organization can help anyone determine if gender equity is being achieved - in businesses and organizations, in the planning and implementation of programs and services, and in the development and enforcement of public policy.
Updates

Apologies for the delay - have not had time to finalize the decision.  Should be early this week - probably Tuesday.

Industry/Entity Type

Business

Requirements
Must have
• New Logo for ParityLumen
• Logo plus words "Fairness Metrics Insight"

```html
<!DOCTYPE html>
<html lang="en">
<head>
<meta charset="utf-8">
<title>ParityLumen Business Card</title>
<link href="https://fonts.googleapis.com/css2?family=Open+Sans:wght@400;600;700&display=swap" rel="stylesheet">
<style>
  :root {
    --orange: #f7941d;
    --orange-deep: #e9830c;
    --ink: #3a3a3a;
    --muted: #6b6b6b;
    --silver: #cfcfcf;
    --paper: #ffffff;
    --backdrop: #e6e6e6;
  }
  * { margin: 0; padding: 0; box-sizing: border-box; }
  html, body { width: 1200px; height: 1024px; overflow: hidden; }
  body {
    background: var(--backdrop);
    font-family: "Open Sans", Arial, sans-serif;
    position: relative;
  }
  .card {
    position: absolute;
    left: 250px;
    width: 700px;
    height: 400px;
    border-radius: 24px;
    overflow: hidden;
    box-shadow: 0 6px 18px rgba(0,0,0,0.18);
  }
  .card-front { top: 84px; background: var(--paper); }
  .card-back {
    top: 540px;
    background: radial-gradient(circle at 60% 40%, var(--orange) 0%, var(--orange-deep) 100%);
  }
  .front-band { position: absolute; inset: 0; }
  .accent-line {
    position: absolute;
    left: 330px; top: 196px;
    width: 100px; height: 3px;
    background: linear-gradient(90deg, rgba(247,148,29,0), var(--orange));
  }
  .brand {
    position: absolute;
    display: flex;
    align-items: center;
    gap: 16px;
  }
  .brand-dot { border-radius: 50%; flex: none; }
  .brand-name { font-weight: 400; letter-spacing: -0.5px; line-height: 1; }
  .card-front .brand { left: 48px; top: 132px; }
  .card-front .brand-dot { width: 60px; height: 60px; background: var(--orange); }
  .card-front .brand-name { font-size: 46px; color: var(--ink); }
  .person { position: absolute; left: 48px; top: 222px; }
  .person-name {
    font-size: 22px; font-weight: 700; color: var(--orange);
    letter-spacing: 0.5px;
  }
  .person-role { font-size: 16px; color: var(--ink); margin-top: 2px; }
  .person-web {
    display: flex; align-items: center; gap: 7px;
    font-size: 15px; color: var(--ink); margin-top: 4px;
  }
  .contact {
    position: absolute;
    right: 40px; top: 34px;
    list-style: none;
    text-align: right;
  }
  .contact li {
    display: flex; justify-content: flex-end; align-items: center; gap: 8px;
    font-size: 15px; color: var(--muted); line-height: 23px;
  }
  .icon-box {
    width: 13px; height: 13px; border-radius: 2px;
    background: var(--orange);
    display: inline-flex; align-items: center; justify-content: center;
  }
  .card-back .brand { left: 50%; top: 150px; transform: translateX(-50%); }
  .card-back .brand-dot { width: 72px; height: 72px; background: var(--paper); }
  .card-back .brand-name { font-size: 60px; color: var(--paper); }
  .back-ring {
    position: absolute; left: 240px; top: 40px;
    width: 320px; height: 320px; border-radius: 50%;
    border: 36px solid rgba(255,255,255,0.07);
  }
  .back-web {
    position: absolute; left: 210px; top: 262px;
    font-size: 16px; color: var(--paper);
  }
</style>
</head>
<body>

<section class="card card-front" aria-label="Card front">
  <svg class="front-band" viewBox="0 0 700 400" width="700" height="400" aria-hidden="true">
    <path d="M0 366 C 260 352 520 250 700 8 L700 30 C 525 262 265 372 0 382 Z" fill="var(--silver)"/>
    <path d="M0 384 C 268 374 530 268 700 34 L700 400 L0 400 Z" fill="var(--orange)"/>
  </svg>
  <div class="accent-line"></div>

  <div class="brand">
    <span class="brand-dot"></span>
    <span class="brand-name">ParityLumen</span>
  </div>

  <div class="person">
    <p class="person-name">MARCUS VELL</p>
    <p class="person-role">Job Title</p>
    <p class="person-web">
      <svg width="13" height="13" viewBox="0 0 14 14" aria-hidden="true">
        <circle cx="7" cy="7" r="6" fill="none" stroke="var(--orange)" stroke-width="1.6"/>
        <path d="M1 7 H13 M7 1 C4 4 4 10 7 13 M7 1 C10 4 10 10 7 13" fill="none" stroke="var(--orange)" stroke-width="1.1"/>
      </svg>
      www.paritylumen.com
    </p>
  </div>

  <ul class="contact">
    <li>000.000.0000
      <span class="icon-box"><svg width="9" height="9" viewBox="0 0 10 10" aria-hidden="true"><path d="M2 1 L4 1 L4.6 3.2 L3.4 4 C4 5.4 4.6 6 6 6.6 L6.8 5.4 L9 6 L9 8 C5 8.5 1.5 5 2 1 Z" fill="#fff"/></svg></span>
    </li>
    <li>000.000.0000
      <span class="icon-box"><svg width="9" height="9" viewBox="0 0 10 10" aria-hidden="true"><path d="M2 1 L4 1 L4.6 3.2 L3.4 4 C4 5.4 4.6 6 6 6.6 L6.8 5.4 L9 6 L9 8 C5 8.5 1.5 5 2 1 Z" fill="#fff"/></svg></span>
    </li>
    <li>@Parity_Lumen <span class="icon-box"></span></li>
    <li>email@paritylumen.com
      <span class="icon-box"><svg width="9" height="9" viewBox="0 0 10 10" aria-hidden="true"><rect x="1" y="2.5" width="8" height="5.5" fill="none" stroke="#fff" stroke-width="1"/><path d="M1 2.5 L5 5.5 L9 2.5" fill="none" stroke="#fff" stroke-width="1"/></svg></span>
    </li>
  </ul>
</section>

<section class="card card-back" aria-label="Card back">
  <div class="back-ring"></div>
  <div class="brand">
    <span class="brand-dot"></span>
    <span class="brand-name">ParityLumen</span>
  </div>
  <p class="back-web">www.paritylumen.com</p>
</section>

</body>
</html>
```